Modern Website Design for PollBeacon – CX & Loyalty SaaS Platform

We need a modern, professional, and responsive website design for our B2B SaaS platform, PollBeacon. We help companies collect real-time customer feedback, analyze insights, and improve loyalty — combining a powerful CX platform with expert consulting services. The website should clearly communicate who we are and what we offer within the first impression. It should balance data-driven visuals such as dashboards, analytics, and charts with a human, approachable feel. The design must include at least six key pages: Homepage, Product/Services, About, Blog/Resources, Contact/Demo, and Pricing. It should be conversion-focused with clear calls-to-action that encourage visitors to request a demo or contact us. The site must be fully responsive across desktop, tablet, and mobile. It should support multiple languages, starting with English and Danish. Most importantly, the delivery must be a final WordPress website, ready to go live, not just design files.

Target Market(s)

Our target market is medium-to-large B2B organizations. The primary audience includes CX leaders, executives, and managers in customer success and service who want to measure loyalty, understand customer insights, and improve retention.

Industry/Entity Type

Technology / SaaS / Customer Experience

Coding

Coded - Design and coding required

Number of Pages Required

5+ page

Font styles to use
Sans Serif

Requirements
Must have
• The project must deliver a final WordPress website that is fully responsive across all devices. The design should be clean, modern, and SaaS-inspired, with clear calls-to-action on every page. It must also support English and Danish, with a visible language toggle. The site should include visuals of dashboards and analytics that reflect data-driven insights. It must feature sections for case studies or testimonials to build trust. The copywriting should be SEO-friendly, and the design should include smooth animations or hover effects that add polish without making the website feel heavy.
Should not have
• Cluttered layouts, or generic stock photos such as handshakes

```html
<!DOCTYPE html>
<html lang="en">
<head>
<meta charset="utf-8">
<title>PollBeacon – CX &amp; Loyalty Platform</title>
<link href="https://fonts.googleapis.com/css2?family=Archivo+Black&family=Montserrat:wght@400;500;600;700;800&display=swap" rel="stylesheet">
<style>
:root{
  --navy:#1b1646;
  --blue:#1f5bb0;
  --deep:#0f2350;
  --orange:#fc3d0a;
  --pale:#e6ecf5;
  --text:#3b3b4a;
  --white:#fff;
}
*{margin:0;padding:0;box-sizing:border-box}
html,body{width:1200px;height:3297px;overflow:hidden}
body{position:relative;font-family:'Montserrat',sans-serif;color:var(--text);background:var(--white)}
.abs{position:absolute}
.btn{position:absolute;display:flex;align-items:center;justify-content:center;background:var(--white);border:2px solid var(--orange);border-radius:7px;color:var(--navy);font-weight:500;font-size:18px;text-decoration:none}
.mark{position:absolute;width:26px;height:26px;border:4px solid var(--orange);transform:rotate(45deg)}
.section-title{position:absolute;left:0;width:1200px;text-align:center;font-weight:700;font-size:44px;letter-spacing:1px;color:var(--navy)}

/* hero */
.hero-bg{position:absolute;left:0;top:0;width:1200px;height:715px}
.brand{position:absolute;left:111px;top:66px;display:flex;align-items:center;gap:8px;font-weight:800;font-size:22px;color:var(--white)}
.brand i{width:16px;height:16px;background:var(--orange);display:block}
.nav{position:absolute;left:312px;top:68px;display:flex;gap:25px;font-size:18px;font-weight:500;color:var(--white)}
.nav .active{color:var(--orange)}
.lang{display:flex;align-items:center;gap:6px}
.hero-title{position:absolute;left:111px;top:210px;font-family:'Archivo Black',sans-serif;font-size:56px;line-height:60px;color:var(--white);letter-spacing:1px}
.hero-text{position:absolute;left:111px;top:408px;width:460px;font-family:Arial,sans-serif;font-size:15.5px;line-height:20px;color:var(--white)}

/* who */
.who-visual{position:absolute;left:155px;top:862px;width:312px;height:312px;transform:rotate(45deg);border-radius:18px;background:linear-gradient(135deg,#0e2c55,#1c6fb8 50%,#0b1d3a)}
.who-title{position:absolute;left:588px;top:842px;font-weight:700;font-size:44px;color:var(--navy);letter-spacing:1px}
.who-text{position:absolute;left:600px;top:918px;width:490px;font-size:18px;line-height:30px}

/* offer */
.offer{position:absolute;left:0;top:1306px;width:1200px;height:568px;background:var(--pale)}
.step{position:absolute;width:200px;text-align:center}
.ring{position:absolute;width:142px;height:142px;border-radius:50%;background:var(--white);border:4px solid var(--orange);border-right-color:var(--blue);border-bottom-color:var(--blue);box-shadow:0 0 0 5px #fff}
.ring span{position:absolute;left:26px;top:26px;width:82px;height:82px;border-radius:50%;background:radial-gradient(circle,#f6c2b0,#fde9e2 70%)}
.step h3{font-size:18px;font-weight:700;color:var(--navy);letter-spacing:.5px;margin-bottom:13px}
.step p{font-size:18px;line-height:26px}

/* testimonials */
.card{position:absolute;top:2122px;width:470px;height:174px;border-radius:90px;border:2px solid #dcdfe6;background:var(--white)}
.card .photo{position:absolute;left:13px;top:14px;width:142px;height:142px;border-radius:50%;background:linear-gradient(160deg,#cfd6df,#2a3c5c)}
.card .stars{position:absolute;left:178px;top:18px;color:var(--orange);font-size:19px;letter-spacing:2px}
.card p{position:absolute;left:178px;top:56px;width:275px;font-size:13.5px;line-height:20px}
.card h4{position:absolute;left:180px;top:130px;font-size:13.5px;font-weight:700;color:#111}
.dot{position:absolute;top:2340px;width:18px;height:18px;border-radius:50%;border:1.5px solid #aab}
.dot.on{background:var(--orange);border-color:var(--orange)}

/* pricing */
.pricing-bg{position:absolute;left:0;top:2423px;width:1200px;height:411px}
.pricing-title{position:absolute;left:0;top:2548px;width:1200px;text-align:center;font-size:40px;font-weight:700;color:var(--white);letter-spacing:1px}
.pricing-text{position:absolute;left:150px;top:2612px;width:900px;text-align:center;font-size:17px;line-height:25.6px;color:var(--white)}

/* footer */
.foot-brand{position:absolute;left:122px;top:2985px;display:flex;align-items:center;gap:14px;font-weight:800;font-size:44px;color:#111;letter-spacing:1px}
.foot-brand i{width:30px;height:30px;background:var(--blue);display:block}
.foot-h{position:absolute;top:2892px;font-size:22px;font-weight:600;color:var(--navy);letter-spacing:.5px}
.foot-h::after{content:"";position:absolute;left:0;top:38px;width:44px;height:2px;background:var(--blue)}
.links{position:absolute;left:539px;top:2947px;list-style:none;font-family:Arial,sans-serif;font-size:15px;color:#222}
.links li{height:32.5px;display:flex;align-items:center;gap:14px}
.links li::before{content:"»";color:var(--orange);font-size:15px}
.contact{position:absolute;left:836px;display:flex;gap:14px;font-size:16px;line-height:25px;color:#222}
.contact svg{flex:none;margin-top:4px}
.rule{position:absolute;left:111px;top:3183px;width:977px;height:1px;background:#e3e3e8}
.copy{position:absolute;left:0;top:3217px;width:1200px;text-align:center;font-size:15.5px;color:#222}
</style>
</head>
<body>

<!-- hero -->
<svg class="hero-bg" viewBox="0 0 1200 715">
  <defs>
    <linearGradient id="heroShade" x1="0" y1="0" x2="1" y2="0">
      <stop offset="0" stop-color="#1b4b8f"/>
      <stop offset=".45" stop-color="#1a2a55"/>
      <stop offset="1" stop-color="#27324a"/>
    </linearGradient>
  </defs>
  <polygon points="0,0 1200,0 1200,548 600,712 0,548" fill="var(--blue)"/>
  <polygon points="0,0 1200,0 1200,540 600,672 0,540" fill="url(#heroShade)" role="img" aria-label="Photo of a laptop showing analytics dashboards with bar, pie and area charts"/>
</svg>
<div class="brand"><i></i>POLLBEACON</div>
<nav class="nav">
  <span class="active">Home</span><span>Services</span><span>About</span><span>Resources</span><span>Pricing</span><span>Contact</span>
  <span class="lang">EN <svg width="10" height="7" viewBox="0 0 10 7"><path d="M0 0h10L5 7z" fill="#fff"/></svg></span>
</nav>
<a class="btn" style="left:932px;top:58px;width:153px;height:46px">Book Demo</a>
<h1 class="hero-title">POLLBEACON IS<br>A B2B CUSTOMER<br>EXPERIENCE</h1>
<p class="hero-text">Sed ut perspiciatis unde omnis iste natus error sit voluptatem accusantium doloremque laudantium</p>
<a class="btn" style="left:116px;top:481px;width:221px;height:45px">Get Started for free</a>

<!-- who we are -->
<div class="who-visual" role="img" aria-label="Diamond-shaped photo of a hand touching floating analytics charts"></div>
<div class="mark" style="left:598px;top:787px"></div>
<h2 class="who-title">WHO WE ARE</h2>
<p class="who-text">PollBeacon is a B2B customer experience (CX) and loyalty platform combined with expert consulting services. We collect real-time feedback, segment insights, and provide leadership-ready reporting with churn-risk alerts. Unlike software-only tools, our platform includes CX experts who help businesses implement, interpret, and act on insights.</p>
<a class="btn" style="left:600px;top:1160px;width:151px;height:46px">Read More</a>

<!-- what we offer -->
<section class="offer"></section>
<div class="mark" style="left:587px;top:1368px"></div>
<h2 class="section-title" style="top:1410px">WHAT WE OFFER</h2>

<div class="ring" style="left:134px;top:1516px"><span role="img" aria-label="Icon of a person at a desk giving feedback"></span></div>
<div class="ring" style="left:395px;top:1516px"><span role="img" aria-label="Icon of gears processing data"></span></div>
<div class="ring" style="left:656px;top:1516px"><span role="img" aria-label="Icon of a lightbulb with connected nodes"></span></div>
<div class="ring" style="left:917px;top:1516px"><span role="img" aria-label="Icon of a launching rocket"></span></div>

<svg class="abs" style="left:290px;top:1555px" width="100" height="40" viewBox="0 0 100 40"><path d="M6 28 Q40 -2 86 26" fill="none" stroke="var(--blue)" stroke-width="2.5"/><path d="M78 30 L88 27 L86 17" fill="none" stroke="var(--blue)" stroke-width="2.5"/></svg>
<svg class="abs" style="left:551px;top:1565px" width="100" height="40" viewBox="0 0 100 40"><path d="M6 10 Q45 40 86 12" fill="none" stroke="var(--blue)" stroke-width="2.5"/><path d="M77 8 L88 10 L85 20" fill="none" stroke="var(--blue)" stroke-width="2.5"/></svg>
<svg class="abs" style="left:812px;top:1555px" width="100" height="40" viewBox="0 0 100 40"><path d="M6 28 Q40 -2 86 26" fill="none" stroke="var(--blue)" stroke-width="2.5"/><path d="M78 30 L88 27 L86 17" fill="none" stroke="var(--blue)" stroke-width="2.5"/></svg>

<div class="step" style="left:105px;top:1682px"><h3>INPUT</h3><p>Sed ut perspiciatis unde omnis iste natus error sit</p></div>
<div class="step" style="left:366px;top:1682px"><h3>PROCESSING</h3><p>Sed ut perspiciatis unde omnis iste natus error sit</p></div>
<div class="step" style="left:627px;top:1682px"><h3>INSIGHTS</h3><p>Sed ut perspiciatis unde omnis iste natus error sit</p></div>
<div class="step" style="left:888px;top:1682px"><h3>ACTION</h3><p>Sed ut perspiciatis unde omnis iste natus error sit</p></div>

<!-- testimonials -->
<div class="mark" style="left:587px;top:1975px"></div>
<h2 class="section-title" style="top:2024px">OUR TESTIMONIALS</h2>
<div class="card" style="left:113px">
  <div class="photo" role="img" aria-label="Portrait photo of a client in a suit"></div>
  <div class="stars">★★★★★</div>
  <p>Sed ut perspiciatis unde omnis iste natus error sit voluptatem accusantium doloremque</p>
  <h4>Mara Lindqvist</h4>
</div>
<div class="card" style="left:616px">
  <div class="photo" role="img" aria-label="Portrait photo of a client in a suit"></div>
  <div class="stars">★★★★★</div>
  <p>Sed ut perspiciatis unde omnis iste natus error sit voluptatem accusantium doloremque</p>
  <h4>Mara Lindqvist</h4>
</div>
<span class="dot" style="left:531px"></span>
<span class="dot on" style="left:565px"></span>
<span class="dot" style="left:594px"></span>
<span class="dot" style="left:623px"></span>
<span class="dot" style="left:651px"></span>

<!-- pricing -->
<svg class="pricing-bg" viewBox="0 0 1200 411"><polygon points="0,92 600,0 1200,92 1200,411 0,411" fill="var(--orange)"/></svg>
<div class="mark" style="left:587px;top:2494px;border-color:#fff"></div>
<h2 class="pricing-title">OUR PRICING</h2>
<p class="pricing-text">Sed ut perspiciatis unde omnis iste natus error sit voluptatem accusantium doloremque laudantium, totam rem aperiam, eaque ipsa quae ab illo inventore veritatis et quasi architecto beatae vitae dicta sunt explicabo. Nemo enim ipsam voluptatem quia voluptas sit aspernatur aut odit aut fugit</p>
<a class="btn" style="left:503px;top:2726px;width:195px;height:46px;border-color:#fff">Request a Demo</a>

<!-- footer -->
<div class="foot-brand"><i></i>POLLBEACON</div>
<h3 class="foot-h" style="left:539px">QUICK LINKS</h3>
<ul class="links"><li>Home</li><li>Services</li><li>About</li><li>Resources</li><li>Pricing</li><li>Contact</li></ul>
<h3 class="foot-h" style="left:833px">GET IN TOUCH</h3>
<div class="contact" style="top:2945px">
  <svg width="16" height="18" viewBox="0 0 16 18"><path d="M8 0a6 6 0 0 1 6 6c0 4.5-6 12-6 12S2 10.5 2 6a6 6 0 0 1 6-6z" fill="var(--orange)"/><circle cx="8" cy="6" r="2.3" fill="#fff"/></svg>
  <span>225 Nemo enim ipsam<br>voluptatem sit 3 2771</span>
</div>
<div class="contact" style="top:3028px">
  <svg width="16" height="16" viewBox="0 0 16 16"><path d="M3 0l3 3-1.6 2.6a10 10 0 0 0 5 5L12 9l4 3-2 3.5C7 16 0 9 0.5 2z" fill="var(--orange)"/></svg>
  <span>+1 555-014-2270</span>
</div>
<div class="contact" style="top:3095px">
  <svg width="18" height="14" viewBox="0 0 18 14"><rect width="18" height="14" rx="2" fill="var(--orange)"/><path d="M1 2l8 6 8-6" fill="none" stroke="#fff" stroke-width="1.6"/></svg>
  <span>info@pollbeacon.com</span>
</div>
<div class="rule"></div>
<p class="copy">Copyright 2025. Company Name. All Rights Reserved</p>

</body>
</html>
```